Business card design needed

I am a small start up business in the mortgage broking industry based in Sydney called 'nest2keys'. I will be providing residential mortgages to first home owners, investors and people looking to refinance. I would like to see designs that use the colors blue, black, and white - same as my logo (see logo design uploaded)

Target Market(s)

My target market is First Home Owners, property investors, and people looking to refinance. The loans I will be providing are for residential property only at this stage, and my clients will predominantly be in the 30-50yr age bracket.

Industry/Entity Type

Residential

Contact Information for Business Card

Owen Presley
Director/Mobile Mortgage Broker
nests2keys
PO BOX 2984
West Calder NSW 2175
Mb: 0471 286 904
email: owen@brickvaleplex.com.au

Requirements
Must have
• please use lower case for business name (i.e. nests2keys)

```html
<!DOCTYPE html>
<html lang="en">
<head>
<meta charset="utf-8">
<title>nests2keys business card</title>
<link href="https://fonts.googleapis.com/css2?family=Questrial&family=Sorts+Mill+Goudy&display=swap" rel="stylesheet">
<style>
  :root {
    --ink: #0a0a0a;
    --paper: #ffffff;
    --aqua: #00ffff;
    --aqua-pale: #7ffdff;
    --edge: #d8d8d8;
  }
  * { margin: 0; padding: 0; box-sizing: border-box; }
  html, body {
    width: 1200px;
    height: 741px;
    overflow: hidden;
    background: var(--paper);
  }
  .card {
    position: relative;
    width: 1200px;
    height: 741px;
    background: var(--paper);
    border: 1px solid var(--edge);
    overflow: hidden;
  }
  .brand {
    position: absolute;
    top: 0;
    left: 0;
    width: 1200px;
    height: 528px;
    display: flex;
    align-items: center;
    justify-content: center;
    gap: 26px;
    padding-bottom: 40px;
  }
  .brand-mark {
    width: 70px;
    height: 70px;
    background: var(--aqua);
  }
  .brand-name {
    font-family: "Questrial", sans-serif;
    font-size: 138px;
    line-height: 1;
    letter-spacing: -2px;
    color: var(--ink);
  }
  .contact-band {
    position: absolute;
    left: 0;
    top: 528px;
    width: 1200px;
    height: 213px;
    background: var(--aqua);
    overflow: hidden;
  }
  .band-name {
    position: absolute;
    left: 18px;
    top: 88px;
    font-family: "Questrial", sans-serif;
    font-size: 190px;
    line-height: 1;
    letter-spacing: -3px;
    color: var(--aqua-pale);
    white-space: nowrap;
  }
  .contact {
    position: relative;
    font-family: "Sorts Mill Goudy", serif;
    color: var(--ink);
    text-align: center;
  }
  .contact-line { white-space: nowrap; }
  .contact-main {
    padding-top: 42px;
    font-size: 31px;
    letter-spacing: 1.6px;
  }
  .contact-address {
    padding-top: 18px;
    font-size: 27px;
    letter-spacing: 1.5px;
  }
  .contact-web {
    padding-top: 8px;
    font-size: 25px;
    letter-spacing: 2px;
  }
</style>
</head>
<body>
  <div class="card">
    <header class="brand">
      <span class="brand-mark"></span>
      <h1 class="brand-name">nests2keys</h1>
    </header>
    <section class="contact-band">
      <div class="band-name" aria-hidden="true">nests2keys</div>
      <div class="contact">
        <p class="contact-line contact-main">owen presley | +61 471 286 904 | owen@nests2keys.com</p>
        <p class="contact-line contact-address">AddressAddressAddressAddressAddressAddressAddressAddress</p>
        <p class="contact-line contact-web">www.nests2key.com | 0532 814 7096</p>
      </div>
    </section>
  </div>
</body>
</html>
```